Short term Rentals Marketing agency needs Web design.

We Need a web design for our new company based in Calgary, AB. We are a International Luxury home sharing company (short term rental properties, Villas, Boutique Hotels, Bed & Breakfast, Realtors, Mortgage Brokers). We would like to see designs that look simple, modern and professional. Colors would be bold (red, black, white). The final design should communicate something welcoming, symbolize innovation, and growth. Our goal is to form partnerships with Real Estate, Property Management, Short term Rental Clients to make their lives easier and increase revenue. Vlto Harbor Co. offers a flexible and secure way to market our clients properties while maintaining client satisfaction and amazing customer service. We like how https://plumtrellisads.ca/ is interactive (when you scroll down, text gets larger). Other similar websites for Short Term Rentals is https://www.thekeyhavenfirm.com/, https://stayvorabnb.com/, https://www.nestquill.com/, https://www.roostfinch.com/about-us/, https://lodgewardens.com. We have attached our Logo.

Target Market(s)

short term rental properties, Villas, Boutique Hotels, Bed & Breakfast, Realtors, Mortgage Brokers, property owners

Industry/Entity Type

Real Estate

Coding

Coded - Design and coding required

Number of Pages Required

5+ page

Font styles to use
Sans Serif

Requirements
Must have
• Home Page, About Us page, How it works, Services, Contact us.

We like how https://plumtrellisads.ca/ is interactive (when you scroll down, text gets larger).

We have attached our Webcopy. We would like Call to Action Buttons where they're located in the copy and page.

Must have our Logo Colors.

Other similar websites for Short Term Rentals is https://www.thekeyhavenfirm.com/, https://stayvorabnb.com/, https://www.nestquill.com/, https://www.roostfinch.com/about-us/, https://lodgewardens.com.
Nice to have
• Catchy, Interactive Home page.

Should not have
• Should not be too cluttered

```html
<!DOCTYPE html>
<html lang="en">
<head>
<meta charset="utf-8">
<title>Vlto Harbor Co. — About Us</title>
<link href="https://fonts.googleapis.com/css2?family=Nunito:wght@400;600&family=Playfair+Display:wght@700&display=swap" rel="stylesheet">
<style>
:root{
  --red:#e3262e;
  --ink:#1b1b1b;
  --text:#2a2a2a;
  --muted:#6d6d6d;
  --soft:#f8f8fb;
  --white:#ffffff;
  --rule:#cfcfcf;
}
*{margin:0;padding:0;box-sizing:border-box}
html,body{width:1200px;height:2518px;overflow:hidden;background:var(--white)}
body{position:relative;font-family:'Nunito',sans-serif;color:var(--text)}
.section{position:absolute;left:0;width:1200px}
.abs{position:absolute}
.heading{font-family:'Playfair Display',serif;font-weight:700;color:var(--ink);font-size:34px;letter-spacing:.6px;line-height:1.2;white-space:nowrap}
.copy{font-size:16.5px;line-height:23.7px;color:var(--text);letter-spacing:.2px;white-space:nowrap}
.photo{position:absolute}

/* hero */
.hero{top:0;height:572px;background:var(--white)}
.hero-photo{left:0;top:0;width:544px;height:572px;background:linear-gradient(160deg,#dde6f0 0%,#eef1f6 45%,#d9dde3 75%,#9aa884 100%)}
.brand{left:55px;top:22px;display:flex;align-items:center;gap:8px}
.brand-mark{width:22px;height:22px;background:var(--red)}
.brand-name{font-size:20px;font-weight:600;color:var(--ink)}
.nav{left:620px;top:36px;display:flex;gap:42px;font-size:15px;color:var(--ink)}
.nav a{color:inherit;text-decoration:none}
.nav a.current{color:var(--muted)}
.contact-btn{left:994px;top:28px;width:149px;height:37px;border:1px solid var(--ink);font-size:15px;color:var(--ink);display:flex;align-items:center;justify-content:center}
.scroll-down{left:620px;top:417px;display:flex;align-items:center;gap:10px;color:var(--red);font-size:15px}
.scroll-down .line{width:34px;height:1px;background:var(--red)}

/* feature blocks */
.feature-soft{background:var(--soft)}
.service{top:572px;height:515px}
.service .photo{left:673px;top:52px;width:432px;height:412px;background:linear-gradient(135deg,#e8e7e4,#d2d0cc 50%,#3b3f4a)}
.innovation{top:1087px;height:513px;background:var(--white)}
.innovation .photo{left:101px;top:49px;width:432px;height:413px;background:linear-gradient(135deg,#eeeae4,#c9a27a 55%,#e7d9c4)}
.skills{top:1600px;height:514px}
.skills .photo{left:673px;top:51px;width:432px;height:412px;background:linear-gradient(135deg,#c99a67,#e8d4b8 50%,#b27b4d)}

.cta{left:100px;top:348px;display:flex;align-items:center;gap:10px;color:var(--red);font-size:17px;padding-bottom:4px;border-bottom:1.5px solid var(--red);width:155px}

/* footer */
.footer{top:2114px;height:404px;background:var(--white)}
.foot-col{position:absolute;top:82px}
.foot-col h4{font-family:'Playfair Display',serif;font-size:23px;font-weight:700;color:#333;margin-bottom:23px}
.foot-col ul{list-style:none;font-size:16.5px;color:var(--ink)}
.foot-col li{height:32.5px}
.socials{display:flex;gap:21px}
.socials span{width:25px;height:25px;border-radius:50%;background:var(--ink)}
.socials span.first{background:var(--red)}
.foot-rule{left:0;top:285px;width:1200px;height:1px;background:var(--rule)}
.legal{left:53px;top:318px;font-size:16.5px;color:#444;display:flex;gap:18px}
.rights{right:53px;top:318px;font-size:16.5px;color:#444}
</style>
</head>
<body>

<section class="section hero">
  <div class="photo hero-photo" role="img" aria-label="Modern white multi-storey building with glass balconies against a pale sky"></div>
  <div class="abs brand"><span class="brand-mark"></span><span class="brand-name">Vlto Harbor Co.</span></div>
  <nav class="abs nav">
    <a class="current" href="#">About us</a>
    <a href="#">Our Services</a>
    <a href="#">How it works</a>
  </nav>
  <div class="abs contact-btn">Contact Us</div>
  <h1 class="abs heading" style="left:620px;top:172px">About Us</h1>
  <p class="abs copy" style="left:620px;top:239px">Vlto Harbor Co. offers you a flexible and secure way<br>to oversee and manage and market your<br>short-term rental properties. We have the skills<br>needed to get our clients the absolute best value<br>for their money, because we give our 110% to each<br>and every one of our valued property owners.<br>Some of the things that set us apart include:</p>
  <div class="abs scroll-down"><span class="line"></span>Scroll down
    <svg width="10" height="7" viewBox="0 0 10 7"><path d="M1 1l4 4 4-4" fill="none" stroke="currentColor" stroke-width="1.6"/></svg>
  </div>
</section>

<section class="section feature-soft service">
  <h2 class="abs heading" style="left:102px;top:164px">Amazing Customer Service</h2>
  <p class="abs copy" style="left:102px;top:232px">Your satisfaction is our first priority – that’s why we<br>always keep an open line of communication<br>between our team members and clients. You’re<br>welcome to contact us with any questions,<br>compliments, or complaints!</p>
  <div class="photo" role="img" aria-label="Business people shaking hands across an office table with laptops and coffee cups"></div>
</section>

<section class="section innovation">
  <div class="photo" role="img" aria-label="Team meeting around a wooden table in front of a cork board with sticky notes"></div>
  <h2 class="abs heading" style="left:645px;top:143px">Innovation and Creativity</h2>
  <p class="abs copy" style="left:645px;top:211px">We pride ourselves on our unbridled creativity when it<br>comes to finding new and innovative ways<br>for you to capitalize on your short-term rental<br>properties. No matter the circumstances, Vlto<br>Harbor Co. will find the best solutions and services for<br>your property’s unique requirements.</p>
</section>

<section class="section feature-soft skills">
  <h2 class="abs heading" style="left:102px;top:142px">Knowledge and Skills</h2>
  <p class="abs copy" style="left:102px;top:210px">We have the skills and knowledge we need to<br>successfully manage your property and get you the<br>most value out of your investment. You’ll gain all the<br>benefits of working with a skilled and professional<br>team, without the hassle or costs of working alone.</p>
  <div class="abs cta">Lets Get Started
    <svg width="13" height="13" viewBox="0 0 13 13"><circle cx="6.5" cy="6.5" r="5.6" fill="none" stroke="#1b1b1b" stroke-width="1.1"/><path d="M5.3 4l2.6 2.5-2.6 2.5" fill="none" stroke="#1b1b1b" stroke-width="1.1"/></svg>
  </div>
  <div class="photo" role="img" aria-label="Hands reviewing printed charts and reports on a wooden desk beside a coffee mug"></div>
</section>

<footer class="section footer">
  <div class="foot-col" style="left:53px"><h4>Company</h4><ul><li>About Us</li><li>Services</li><li>How it works</li><li>Contact</li></ul></div>
  <div class="foot-col" style="left:329px"><h4>Inspiration</h4><ul><li>Blog</li><li>Gallary</li><li>Testimonials</li></ul></div>
  <div class="foot-col" style="left:611px"><h4>Help</h4><ul><li>FAQS</li><li>Customers support</li></ul></div>
  <div class="foot-col" style="left:856px"><h4>Social media</h4><div class="socials"><span class="first"></span><span></span><span></span></div></div>
  <div class="abs foot-rule"></div>
  <div class="abs legal"><span>Privacy Policy</span><span>Customer Agreement</span></div>
  <div class="abs rights">© 2020 All Rights Reserved</div>
</footer>

</body>
</html>
```